Cardiology Practice needs a Heart Scan Order Form

Busy cardiology practice needs an order form for a heart scan test. Sample is attached. One side should have all information noted and the other side should have our physician names (Vikram Joshi, MD, K.L. Morvandi, MD, Anjali Desai, MD, Parvin Joshi, MD, and Gerald Montefino, MD. It should have the map that is uploaded and our demographic information (Crestline Cardio PLLC, 218 Juniper Ave. Ste. B, Webster, TX 77412 along with phone 713-642-1187 and fax 713-642-1188) as well as our web address (crestlinecardio.example). Our primary colors are red, black and white. Needs to fit paper size 8 1/2 by 11.

Target Market(s)

Healthcare

Industry/Entity Type

Health Care

Font styles to use
Serif

Colors
ec1f27

Requirements
Must have
• Logo, information listed on sample form, demographics and physician names as well as website.
Nice to have
• Open to suggestions
Should not have
• Physician Pictures

```html
<!DOCTYPE html>
<html lang="en">
<head>
<meta charset="utf-8">
<title>Crestline Cardio – Calcium Score Heart Scan Order Form</title>
<link rel="stylesheet" href="https://fonts.googleapis.com/css2?family=Montserrat:wght@400;500;600;700;800;900&display=swap">
<style>
:root{
  --red:#c8202e;
  --red-deep:#a91a26;
  --ink:#1f1f1f;
  --grey-band:#ececec;
  --line:#777;
  --backdrop:#e1e4e1;
  --white:#ffffff;
  --dark:#232323;
}
*{box-sizing:border-box;margin:0;padding:0}
html,body{width:1200px;height:3000px;overflow:hidden}
body{background:var(--backdrop);font-family:"Montserrat",sans-serif;color:var(--ink);position:relative}
.page{position:absolute;left:100px;width:1000px;height:1110px;background:var(--white);box-shadow:0 2px 8px rgba(0,0,0,.12);overflow:hidden}
.page--front{top:300px}
.page--back{top:1490px}
.abs{position:absolute}

/* brand */
.brand{display:flex;align-items:center;gap:12px;white-space:nowrap}
.brand__mark{width:20px;height:20px;background:var(--red);border-radius:50%}
.brand__name{font-weight:800;font-size:28px;color:var(--red);letter-spacing:1px;line-height:1}

/* title */
.title{left:453px;top:22px;font-weight:900;font-size:38px;line-height:44px;letter-spacing:.5px;white-space:nowrap}
.title__red{color:var(--red)}
.test-box{top:112px;height:29px;background:var(--grey-band);font-size:14px;padding:6px 8px}

/* bars */
.red-bar{background:var(--red);color:var(--white);font-weight:700;text-align:center}
.physicians{left:51px;top:157px;width:741px;height:32px;font-size:12px;display:flex;justify-content:center;align-items:center;gap:12px;white-space:nowrap}
.physicians span::before{content:"";display:inline-block;width:8px;height:8px;background:var(--white);margin-right:6px}
.section-head{height:26px;background:var(--grey-band);font-weight:700;font-size:14px;text-align:center;line-height:26px}

/* fields */
.field{font-size:11px;display:flex;align-items:flex-end;gap:6px;white-space:nowrap}
.field__line{flex:1;border-bottom:1px solid var(--line);height:12px}
.check{font-size:11px;white-space:nowrap}
.check::before{content:"";display:inline-block;width:7px;height:7px;border:1px solid #555;margin-right:6px;vertical-align:1px}

/* instructions */
.notice{left:51px;top:635px;width:741px;height:42px;font-size:14px;line-height:17px;padding-top:4px}
.rules{font-size:12.5px;line-height:15.5px;width:330px}
.rules p{margin-bottom:14px;padding-left:14px;position:relative}
.rules p.dot::before{content:"";position:absolute;left:0;top:5px;width:5px;height:5px;border-radius:50%;background:var(--red)}
.ack{left:51px;top:872px;width:741px;height:40px;background:var(--grey-band);font-size:12.5px;line-height:15px;text-align:center;padding-top:5px}
.sig{width:225px;border-top:1px solid var(--line);font-size:13px;font-weight:700;text-align:center;padding-top:8px}
.referral{left:608px;top:935px;width:184px;border:1px solid #333;font-size:8px}
.referral div{border-top:1px solid #333;height:28px;padding:6px 3px 0}
.referral .referral__head{border-top:0;height:14px;padding:2px 3px;background:#f4f4f4}
.footer{left:51px;top:1053px;width:741px;height:38px;font-size:12px;font-weight:500;line-height:15px;padding-top:4px}

/* back page */
.red-panel{left:0;top:160px;width:1000px;height:536px;background:linear-gradient(135deg,var(--red) 0%,var(--red-deep) 60%,var(--red) 100%)}
.physician-card{width:213px;height:224px;border:2px solid rgba(255,255,255,.85);display:flex;align-items:flex-end}
.physician-card__name{width:100%;height:34px;background:var(--dark);color:var(--white);font-size:13px;font-weight:700;text-align:center;line-height:34px;white-space:nowrap}
.map{left:0;top:696px;width:437px;height:400px;background:linear-gradient(135deg,#eeece6 0%,#e3e6e8 100%)}
.base-bar{left:0;top:1096px;width:1000px;height:14px;background:var(--dark)}
.contact{left:496px;font-size:22px;font-weight:700;line-height:27px;display:flex;gap:14px;align-items:flex-start;white-space:nowrap}
.contact svg{flex:none;margin-top:4px}
</style>
</head>
<body>

<!-- FRONT: order form -->
<section class="page page--front">
  <div class="abs brand" style="left:53px;top:74px">
    <span class="brand__mark"></span><span class="brand__name">CRESTLINE CARDIO</span>
  </div>

  <h1 class="abs title">CALCIUM SCORE<br><span class="title__red">HEART SCAN</span></h1>
  <div class="abs test-box" style="left:453px;width:166px">Test date:</div>
  <div class="abs test-box" style="left:624px;width:168px">Test time:</div>

  <div class="abs red-bar physicians">
    <span>Vikram Joshi M.D.</span><span>K.L. Morvandi M.D.</span><span>Anjali Desai M.D.</span><span>Parvin Joshi M.D.</span><span>Gerald Montefino, M.D.</span>
  </div>

  <div class="abs section-head" style="left:51px;top:200px;width:363px">Patient information</div>
  <div class="abs section-head" style="left:429px;top:200px;width:363px">Contact information</div>

  <!-- patient -->
  <div class="abs" style="left:60px;top:238px;width:110px;font-size:11px;text-align:center">Last name</div>
  <div class="abs" style="left:177px;top:238px;width:110px;font-size:11px;text-align:center">First name</div>
  <div class="abs" style="left:294px;top:238px;width:110px;font-size:11px;text-align:center">MI</div>
  <div class="abs" style="left:60px;top:268px;width:110px;border-top:1px solid var(--line)"></div>
  <div class="abs" style="left:177px;top:268px;width:110px;border-top:1px solid var(--line)"></div>
  <div class="abs" style="left:294px;top:268px;width:110px;border-top:1px solid var(--line)"></div>
  <div class="abs field" style="left:58px;top:300px;width:160px">Date of birth<span class="field__line"></span></div>
  <div class="abs field" style="left:232px;top:300px;width:172px">Account no.<span class="field__line"></span></div>

  <!-- contact -->
  <div class="abs field" style="left:452px;top:240px;width:340px">Address<span class="field__line"></span></div>
  <div class="abs" style="left:452px;top:276px;width:340px;border-top:1px solid var(--line)"></div>
  <div class="abs field" style="left:452px;top:300px;width:340px">Home phone no.<span class="field__line"></span></div>
  <div class="abs field" style="left:452px;top:327px;width:340px">Mobile phone no.<span class="field__line"></span></div>

  <div class="abs section-head" style="left:51px;top:365px;width:741px">Medical information</div>
  <div class="abs" style="left:58px;top:408px;font-size:11px">Sex:</div>
  <div class="abs check" style="left:88px;top:408px">F</div>
  <div class="abs check" style="left:118px;top:408px">M</div>
  <div class="abs field" style="left:170px;top:408px;width:193px">Height:<span class="field__line"></span></div>
  <div class="abs field" style="left:380px;top:408px;width:192px">Weight:<span class="field__line"></span></div>
  <div class="abs field" style="left:596px;top:408px;width:196px">Race:<span class="field__line"></span></div>
  <div class="abs field" style="left:58px;top:442px;width:734px">Diagnosis:<span class="field__line"></span></div>
  <div class="abs" style="left:58px;top:492px;width:734px;border-top:1px solid var(--line)"></div>

  <div class="abs field" style="left:58px;top:524px;width:236px"><span class="check">PCI (no. of stents</span><span class="field__line"></span>)</div>
  <div class="abs field" style="left:306px;top:524px;width:252px"><span class="check">CABG (no. of vessels:</span><span class="field__line"></span>)</div>
  <div class="abs field" style="left:573px;top:524px;width:219px"><span class="check">MI (last event:</span><span class="field__line"></span>)</div>
  <div class="abs check" style="left:58px;top:561px">PCM/ICD</div>
  <div class="abs check" style="left:170px;top:561px">Diabetes</div>
  <div class="abs check" style="left:293px;top:561px">Claustrophobia</div>
  <div class="abs check" style="left:475px;top:561px">Asthma</div>
  <div class="abs check" style="left:594px;top:561px">Emphysema</div>
  <div class="abs check" style="left:731px;top:561px">COPD</div>
  <div class="abs check" style="left:58px;top:596px">bHCG</div>
  <div class="abs check" style="left:170px;top:596px">Tubal ligation</div>
  <div class="abs check" style="left:293px;top:596px">Post-menopause &gt; 1 year</div>
  <div class="abs check" style="left:475px;top:596px">Hysterectomy</div>
  <div class="abs field" style="left:594px;top:596px;width:198px"><span class="check">LMP:</span><span class="field__line"></span></div>

  <div class="abs red-bar notice">Please read the following instructions carefully. You might be rescheduled if any<br>of the following instructions are not met.</div>

  <div class="abs rules" style="left:60px;top:700px">
    <p class="dot">AVOID caffeine containing products (coffee, tea, soda, chocolate, energy drinks, or some over the counter medications) for 4 hours prior to testing.</p>
    <p>AVOID smoking for 4 hours prior to testing.</p>
    <p>AVOID eating or drinking anything except water for 4 hours prior to testing.</p>
    <p>Arrive 15 minutes early for your appointment time.</p>
  </div>
  <div class="abs rules" style="left:445px;top:700px;width:350px">
    <p class="dot">Wear comfortable clothing. Remove any metal objects, such as jewelry or piercings. Women will be asked to remove bras containing metal underwire.</p>
    <p class="dot">Inform your physician or the staff if you are claustrophobic or have a problem staying in restricted environments for any length of time.</p>
    <p class="dot">Inform the physician or the staff if you are or think you might be pregnant.</p>
  </div>

  <div class="abs ack">I hereby acknowledge that the instructions and procedures pertinent to this study were explained thoroughly,<br>I had time to ask questions, and these questions were addressed satisfactorily.</div>

  <div class="abs sig" style="left:51px;top:948px">Patient’s print name</div>
  <div class="abs sig" style="left:316px;top:948px">Patient’s signature</div>
  <div class="abs sig" style="left:51px;top:1003px">Prescriber’s print name</div>
  <div class="abs sig" style="left:316px;top:1003px">Prescriber’s signature</div>

  <div class="abs referral">
    <div class="referral__head">Referring physician contact information</div>
    <div>Order date:</div>
    <div>Tel no.:</div>
    <div>Fax no.:</div>
  </div>

  <div class="abs red-bar footer">Crestline Cardio, PLLC. Visit us at 218 Juniper Ave. Ste. B, Webster, TX 77412. For appointments or<br>more information on testing, please call (713) 642 1187, or visit www.crestlinecardio.example.</div>
</section>

<!-- BACK: physicians and location -->
<section class="page page--back">
  <div class="abs brand" style="left:300px;top:70px">
    <span class="brand__mark"></span><span class="brand__name">CRESTLINE CARDIO</span>
  </div>

  <div class="abs red-panel"></div>

  <div class="abs physician-card" style="left:96px;top:192px"><div class="physician-card__name">Vikram Joshi, MD</div></div>
  <div class="abs physician-card" style="left:331px;top:192px"><div class="physician-card__name">K.L. Morvandi, MD</div></div>
  <div class="abs physician-card" style="left:563px;top:192px"><div class="physician-card__name">Anjali Desai, MD</div></div>
  <div class="abs physician-card" style="left:202px;top:440px"><div class="physician-card__name">Parvin Joshi, MD</div></div>
  <div class="abs physician-card" style="left:438px;top:440px"><div class="physician-card__name">Gerald Montefino, MD</div></div>

  <div class="abs map" role="img" aria-label="Street map showing the practice location in Webster, TX"></div>

  <div class="abs contact" style="top:792px">
    <svg width="16" height="22" viewBox="0 0 16 22"><path d="M8 0a8 8 0 0 0-8 8c0 6 8 14 8 14s8-8 8-14a8 8 0 0 0-8-8z" fill="var(--red)"/><circle cx="8" cy="8" r="3" fill="#fff"/></svg>
    <div>Crestline Cardio PLLC,<br>218 Juniper Ave. Ste. B,<br>Webster, TX 77412</div>
  </div>
  <div class="abs contact" style="top:888px">
    <svg width="16" height="18" viewBox="0 0 24 24"><path d="M6.6 10.8a15 15 0 0 0 6.6 6.6l2.2-2.2c.3-.3.7-.4 1-.2 1.1.4 2.3.6 3.6.6.6 0 1 .4 1 1V20c0 .6-.4 1-1 1A17 17 0 0 1 3 4c0-.6.4-1 1-1h3.5c.6 0 1 .4 1 1 0 1.3.2 2.5.6 3.6.1.3 0 .7-.2 1z" fill="var(--red)"/></svg>
    <div>713-642-1187</div>
  </div>
  <div class="abs contact" style="top:933px">
    <svg width="16" height="18" viewBox="0 0 16 18"><rect x="0" y="6" width="16" height="12" rx="1" fill="var(--red)"/><rect x="3" y="0" width="10" height="7" fill="var(--red)"/><rect x="3" y="9" width="4" height="2" fill="#fff"/><rect x="9" y="9" width="4" height="2" fill="#fff"/><rect x="3" y="13" width="4" height="2" fill="#fff"/><rect x="9" y="13" width="4" height="2" fill="#fff"/></svg>
    <div>713-642-1188</div>
  </div>
  <div class="abs contact" style="top:984px">
    <svg width="18" height="18" viewBox="0 0 20 20"><circle cx="10" cy="10" r="9" fill="none" stroke="var(--red)" stroke-width="2"/><ellipse cx="10" cy="10" rx="4" ry="9" fill="none" stroke="var(--red)" stroke-width="2"/><line x1="1" y1="10" x2="19" y2="10" stroke="var(--red)" stroke-width="2"/></svg>
    <div>crestlinecardio.example</div>
  </div>

  <div class="abs base-bar"></div>
</section>

</body>
</html>
```